Buff & Gleam

polished concrete and epoxy coatings flooring company

Target Market(s)

Industrial commercial

Industry/Entity Type

Industrial flooring contractor

Contact Information for Business Card

POLISHED CONCRETE • EPOXY COATING • TERRAZZO RESTORATION • SHOT BLASTING • SURFACE PREPARATION • JOINT FILLING • TILE/ CARPET /GLUE REMOVAL

Colors
0054AA
0677BA
7BADD7
CADEEF
E8F1F8

Requirements
Must have
• email buffandgleamfloors@mailbrook.example Address 47215 Tallowmere Rd, Fraser, MI 48093. Name Ray Tulvin. Services Polished concrete- Epoxy Coatings- Terrazzo restoration-surface preparation- safety striping- joint filling- tile/ carpet/ glue removal phone number 586-700-3926 email buffandgleamfloors.example
Nice to have
• Instagram Facebook logo maybe smaller in the corner

```html
<!DOCTYPE html>
<html lang="en">
<head>
<meta charset="utf-8">
<title>Buff &amp; Gleam – Business Card</title>
<link rel="stylesheet" href="https://fonts.googleapis.com/css2?family=Poppins:wght@400;500;700&display=swap">
<style>
  :root {
    --brand-blue: #2570b9;
    --deep-blue: #0054aa;
    --mid-blue: #0677ba;
    --sky-blue: #7badd7;
    --pale-blue: #cadeef;
    --mist-blue: #e8f1f8;
    --ink: #1b1b1b;
    --white: #ffffff;
    --backdrop: #c9c9cb;
  }
  * { box-sizing: border-box; margin: 0; padding: 0; }
  html, body { width: 1200px; height: 1200px; overflow: hidden; }
  body {
    background: var(--backdrop);
    font-family: "Poppins", sans-serif;
    position: relative;
  }
  .card {
    position: absolute;
    left: 150px;
    width: 900px;
    height: 514px;
    background: var(--brand-blue);
    overflow: hidden;
    box-shadow: 0 8px 24px rgba(0,0,0,0.18);
  }
  .card--front { top: 56px; }
  .card--back { top: 630px; }

  /* Front */
  .brand {
    position: absolute;
    left: 0; top: 0;
    width: 360px; height: 100%;
    display: flex; align-items: center; justify-content: center;
  }
  .brand__name {
    color: var(--white);
    font-weight: 700;
    font-size: 42px;
    letter-spacing: 1px;
    text-transform: uppercase;
    line-height: 1.1;
    text-align: center;
  }
  .panel {
    position: absolute;
    left: 372px;
    right: 0;
    background: var(--white);
    border-radius: 34px 0 0 34px;
  }
  .panel--name { top: 22px; height: 196px; }
  .panel--contact { top: 258px; bottom: 0; border-radius: 34px 0 0 0; }
  .panel__tab {
    position: absolute;
    left: 10px; top: 14px; bottom: 14px;
    width: 52px;
    background: var(--brand-blue);
    border-radius: 26px;
    display: flex; flex-direction: column; align-items: center; justify-content: center;
    gap: 14px;
  }
  .panel--contact .panel__tab { bottom: 40px; top: 18px; justify-content: flex-start; padding-top: 22px; gap: 15px; }
  .icon { width: 22px; height: 22px; fill: var(--white); }
  .person-name {
    position: absolute;
    left: 100px; top: 50%;
    transform: translateY(-50%);
    color: var(--brand-blue);
    font-weight: 700;
    font-size: 46px;
    letter-spacing: 1px;
    text-transform: uppercase;
  }
  .contact-list {
    position: absolute;
    left: 96px; top: 40px;
    list-style: none;
    color: var(--ink);
    font-size: 19px;
    line-height: 37px;
  }

  /* Back */
  .services {
    position: absolute;
    left: 0; right: 0; top: 70px;
    text-align: center;
    color: var(--white);
    font-weight: 500;
    font-size: 21px;
    line-height: 42px;
    text-transform: uppercase;
    letter-spacing: 0.3px;
  }
  .gallery {
    position: absolute;
    left: 0; right: 0; bottom: 0;
    height: 214px;
    display: grid;
    grid-template-columns: 1fr 1fr 1fr;
    gap: 14px;
    padding-top: 0;
  }
  .gallery__photo { height: 100%; }
  .gallery__photo--corridor { background: linear-gradient(160deg, #f4ece3, #d9c2a6 60%, #efe6dc); }
  .gallery__photo--kitchen { background: linear-gradient(160deg, #3a3a3a, #8d9094 50%, #c7cacd); }
  .gallery__photo--lobby { background: linear-gradient(160deg, #e9f2ee, #cfe0da 55%, #f4f8f6); }
</style>
</head>
<body>

<section class="card card--front" aria-label="Business card front">
  <div class="brand">
    <p class="brand__name">Buff &amp;<br>Gleam</p>
  </div>

  <div class="panel panel--name">
    <div class="panel__tab">
      <svg class="icon" viewBox="0 0 24 24" aria-hidden="true"><circle cx="12" cy="7" r="5"/><path d="M2 23c0-6 4.5-9 10-9s10 3 10 9z"/></svg>
    </div>
    <h1 class="person-name">Ray Tulvin</h1>
  </div>

  <div class="panel panel--contact">
    <div class="panel__tab">
      <svg class="icon" viewBox="0 0 24 24" aria-hidden="true"><path d="M12 1a8 8 0 0 0-8 8c0 6 8 14 8 14s8-8 8-14a8 8 0 0 0-8-8zm0 11a3 3 0 1 1 0-6 3 3 0 0 1 0 6z"/></svg>
      <svg class="icon" viewBox="0 0 24 24" aria-hidden="true"><path d="M6.6 10.8a15 15 0 0 0 6.6 6.6l2.2-2.2a1 1 0 0 1 1-.3 11 11 0 0 0 3.6.6 1 1 0 0 1 1 1V20a1 1 0 0 1-1 1A17 17 0 0 1 3 4a1 1 0 0 1 1-1h3.5a1 1 0 0 1 1 1c0 1.3.2 2.5.6 3.6a1 1 0 0 1-.3 1z"/></svg>
      <svg class="icon" viewBox="0 0 24 24" aria-hidden="true"><path d="M2 5h20v14H2z" fill="none" stroke="#fff" stroke-width="2"/><path d="M2 5l10 8 10-8" fill="none" stroke="#fff" stroke-width="2"/></svg>
      <svg class="icon" viewBox="0 0 24 24" aria-hidden="true"><g fill="none" stroke="#fff" stroke-width="1.8"><circle cx="12" cy="12" r="10"/><ellipse cx="12" cy="12" rx="4.5" ry="10"/><path d="M2 12h20M4 7h16M4 17h16"/></g></svg>
    </div>
    <ul class="contact-list">
      <li>47215 Tallowmere Rd, Fraser, MI 48093</li>
      <li>586-700-3926</li>
      <li>buffandgleamfloors@mailbrook.example</li>
      <li>buffandgleamfloors.example</li>
    </ul>
  </div>
</section>

<section class="card card--back" aria-label="Business card back">
  <p class="services">
    Polished Concrete | Epoxy Coating | Terrazzo Restoration<br>
    Shot Blasting | Surface Preparation | Joint Filling<br>
    Tile/ Carpet /Glue Removal
  </p>
  <div class="gallery">
    <div class="gallery__photo gallery__photo--corridor" role="img" aria-label="Photo of a bright corridor with a polished patterned floor"></div>
    <div class="gallery__photo gallery__photo--kitchen" role="img" aria-label="Photo of a modern interior with a grey polished concrete floor"></div>
    <div class="gallery__photo gallery__photo--lobby" role="img" aria-label="Photo of a glossy white epoxy-coated lobby floor"></div>
  </div>
</section>

</body>
</html>
```